Unique and original Business Card for Financial Services Business

I have moved premises and need to change the detail on my business card so thought now is a good time for a re-design. Looking for something professional and modern with colours to fit in with out logo. Like the idea of foil or embossing if that works but not a must have but I do want something that stands out and that I could not design myself.

Once business card is designed I will also be looking to get letterhead and flyers done but want the business card concept in place first.

The majority of designs I am receiving are generic and template based. I am looking for something unique and original. We have some great design elements in our logo, think outside the box and show me something that stands out from the crowd.

Target Market(s)

Business Professionals

Industry/Entity Type

Finance

Contact Information for Business Card

Name: Delia Norwood Phone 0473 958 162 Address PO Box 8617 Mossvale NSW 2389 Email info@steadyharbourfinancialservices.com.au website www.steadyharbourfinancialservices.com.au

Font styles to use
Other font styles liked:
• Ralway

Requirements
Should not have
• No black backgrounds please

```html
<!DOCTYPE html>
<html lang="en">
<head>
<meta charset="utf-8">
<title>Steady Harbour Financial Services – Business Card</title>
<link rel="stylesheet" href="https://fonts.googleapis.com/css2?family=Raleway:wght@300&family=Ubuntu:wght@700&family=Encode+Sans+Condensed:wght@300&display=swap">
<style>
  :root {
    --stage: #d8d8d8;
    --paper: #ffffff;
    --navy: #003a52;
    --deep-teal: #005470;
    --teal: #0f8b93;
    --bright-teal: #13a3a6;
    --ink: #555a5e;
  }
  * { margin: 0; padding: 0; box-sizing: border-box; }
  html, body { width: 1200px; height: 846px; overflow: hidden; }
  body {
    background: var(--stage);
    display: flex;
    align-items: center;
    justify-content: center;
    gap: 40px;
  }
  .card {
    position: relative;
    width: 520px;
    height: 318px;
    overflow: hidden;
    box-shadow: 0 10px 28px rgba(0,0,0,.18);
  }
  .card-front { background: var(--paper); }
  .accent-area {
    position: absolute;
    top: 0;
    right: 0;
    width: 240px;
    height: 176px;
    border-bottom-left-radius: 90px;
    background: linear-gradient(225deg, var(--deep-teal) 0%, var(--teal) 60%, var(--bright-teal) 100%);
  }
  .contact {
    position: absolute;
    left: 46px;
    top: 160px;
  }
  .contact-name {
    font-family: "Ubuntu", sans-serif;
    font-weight: 700;
    font-size: 22px;
    color: var(--teal);
    margin-bottom: 10px;
  }
  .contact-list { list-style: none; }
  .contact-item {
    display: flex;
    align-items: center;
    gap: 9px;
    height: 20px;
    font-family: "Encode Sans Condensed", sans-serif;
    font-weight: 300;
    font-size: 13px;
    color: var(--ink);
    white-space: nowrap;
  }
  .contact-icon { width: 14px; height: 14px; fill: var(--teal); flex: none; }

  .card-back {
    background: var(--navy);
    display: flex;
    flex-direction: column;
    align-items: center;
    justify-content: center;
    gap: 8px;
    font-family: "Raleway", sans-serif;
    font-weight: 300;
    color: var(--bright-teal);
  }
  .brand-name { font-size: 36px; letter-spacing: 1px; }
  .brand-tagline { font-size: 17px; letter-spacing: 9px; }
</style>
</head>
<body>
  <section class="card card-front">
    <div class="accent-area" role="img" aria-label="Decorative flowing teal shape in the upper right corner"></div>
    <div class="contact">
      <h1 class="contact-name">Delia Norwood</h1>
      <ul class="contact-list">
        <li class="contact-item">
          <svg class="contact-icon" viewBox="0 0 24 24" aria-hidden="true"><path d="M6.6 10.8a15.1 15.1 0 0 0 6.6 6.6l2.2-2.2a1 1 0 0 1 1-.25 11.4 11.4 0 0 0 3.6.57 1 1 0 0 1 1 1V20a1 1 0 0 1-1 1A17 17 0 0 1 3 4a1 1 0 0 1 1-1h3.5a1 1 0 0 1 1 1c0 1.250.2 2.45.57 3.57a1 1 0 0 1-.25 1z"/></svg>
          0473 958 162
        </li>
        <li class="contact-item">
          <svg class="contact-icon" viewBox="0 0 24 24" aria-hidden="true"><path d="M2 5h20v14H2z"/><path d="M3 6l9 7 9-7" fill="none" stroke="#fff" stroke-width="1.5"/></svg>
          info@steadyharbourfinancialservices.com.au
        </li>
        <li class="contact-item">
          <svg class="contact-icon" viewBox="0 0 24 24" aria-hidden="true"><circle cx="12" cy="12" r="10"/><path d="M2 12h20M12 2c3 3 3 17 0 20M12 2c-3 3-3 17 0 20M4 7h16M4 17h16" fill="none" stroke="#fff" stroke-width="1.3"/></svg>
          www.steadyharbourfinancialservices.com.au
        </li>
        <li class="contact-item">
          <svg class="contact-icon" viewBox="0 0 24 24" aria-hidden="true"><path d="M12 2a7 7 0 0 0-7 7c0 5 7 13 7 13s7-8 7-13a7 7 0 0 0-7-7zm0 9.5A2.5 2.5 0 1 1 12 6.5a2.5 2.5 0 0 1 0 5z"/></svg>
          PO Box 8617 Mossvale NSW 2389
        </li>
      </ul>
    </div>
  </section>

  <section class="card card-back">
    <p class="brand-name">STEADY HARBOUR</p>
    <p class="brand-tagline">Financial Services</p>
  </section>
</body>
</html>
```